I am looking for a modern style design for a podcast cover art.
Titled: Open Harbor with R.K. Thistlewood
colors to stay in the grays, reds, blacks, white, gold, and maybe blues if it fits well. I attached a mock up of what we are going for and a current podcast cover we drew inspiration from.
Colors
3276b5
ec1f27
f04a50
1b1b1b
474747
919191
d2d2d2

```html
<!DOCTYPE html>
<html lang="en">
<head>
<meta charset="utf-8">
<title>Open Harbor with R.K. Thistlewood — Podcast Cover</title>
<link rel="stylesheet" href="https://fonts.googleapis.com/css2?family=Russo+One&family=Bebas+Neue&display=swap">
<style>
  :root {
    --wall-light: #efeeec;
    --wall-mid: #dcdad6;
    --host-light: #8a8a8a;
    --host-dark: #1b1b1b;
    --title-blue: #1659a3;
    --title-black: #1b1b1b;
    --band-blue: #3f6cab;
    --ink-white: #ffffff;
  }
  html, body {
    margin: 0;
    padding: 0;
    overflow: hidden;
    background: #ffffff;
  }
  .cover {
    position: relative;
    width: 1200px;
    height: 848px;
    overflow: hidden;
  }
  .cover__wall {
    position: absolute;
    inset: 0;
    background: radial-gradient(ellipse at 50% 45%, var(--wall-light) 0%, var(--wall-mid) 100%);
  }
  .cover__host-photo {
    position: absolute;
    left: 30px;
    top: 215px;
    width: 640px;
    height: 633px;
    border-radius: 120px 120px 0 0;
    background: linear-gradient(180deg, var(--host-light) 0%, #4a4a4a 35%, var(--host-dark) 100%);
  }
  .cover__title {
    position: absolute;
    left: 0;
    right: 0;
    top: 22px;
    margin: 0;
    text-align: center;
    white-space: nowrap;
    font-family: "Russo One", "Arial Black", sans-serif;
    font-weight: 400;
    font-size: 142px;
    line-height: 1.2;
    letter-spacing: 2px;
    text-transform: uppercase;
  }
  .cover__title-lead { color: var(--title-blue); }
  .cover__title-tail { color: var(--title-black); }
  .cover__with {
    position: absolute;
    left: 800px;
    top: 498px;
    margin: 0;
    font-family: "Bebas Neue", "Arial Narrow", sans-serif;
    font-size: 76px;
    line-height: 1;
    color: var(--title-black);
    letter-spacing: 1px;
  }
  .cover__band {
    position: absolute;
    inset: 0;
  }
  .cover__host-name {
    font-family: "Bebas Neue", "Arial Narrow", sans-serif;
    font-size: 122px;
    fill: var(--ink-white);
    letter-spacing: 2px;
  }
</style>
</head>
<body>
  <main class="cover">
    <div class="cover__wall" role="img" aria-label="White painted brick wall background"></div>
    <div class="cover__host-photo" role="img" aria-label="Black and white photo of the host in a tuxedo and bow tie, pointing to the right"></div>

    <h1 class="cover__title"><span class="cover__title-lead">Open</span><span class="cover__title-tail">Harbor</span></h1>
    <p class="cover__with">WITH</p>

    <svg class="cover__band" width="1200" height="848" viewBox="0 0 1200 848" aria-hidden="false">
      <polygon class="cover__band-shape" points="0,690 1200,560 1200,710 0,848" fill="var(--band-blue)" fill-opacity="0.92"/>
      <text class="cover__host-name" x="805" y="748" text-anchor="middle" transform="rotate(-6.2 805 705)">R.K. THISTLEWOOD</text>
    </svg>
  </main>
</body>
</html>
```